Private Learning Centre in Singapore needs a flyer design

We need a flyer design for our upcoming education fair and also able to use it for day to day purpose. The aim is to attract parents, students to enrol for classes by offering them free trial class/assessment. 2 sided flyer with the front page as the logo only and details on the other page. We would like to see a final design in blue, white and it should be curious and attractive enough not to allow customers to throw it away once they received it.

Education

```html
<!DOCTYPE html>
<html lang="en">
<head>
<meta charset="utf-8">
<title>Bright Grove Academy – Flyer</title>
<link rel="stylesheet" href="https://fonts.googleapis.com/css2?family=Arimo:wght@400;700&display=swap">
<style>
  :root {
    --blue-deep: #1e3796;
    --blue-mid: #3553b0;
    --blue-soft: #8fa4dc;
    --blue-pale: #eef2fb;
    --white: #ffffff;
    --ink: #1b1b1b;
    --backdrop: #e9ebef;
  }
  * { box-sizing: border-box; margin: 0; padding: 0; }
  html, body { width: 1200px; height: 640px; overflow: hidden; }
  body {
    background: var(--backdrop);
    font-family: "Arimo", Arial, sans-serif;
    position: relative;
  }
  .flyer {
    position: absolute;
    top: 127px;
    width: 560px;
    height: 386px;
    overflow: hidden;
    background: var(--white);
    box-shadow: 0 4px 14px rgba(0,0,0,.18);
  }
  /* Front side */
  .flyer--front {
    left: 25px;
    background:
      repeating-linear-gradient(90deg, rgba(255,255,255,.10) 0 14px, rgba(255,255,255,0) 14px 38px),
      linear-gradient(170deg, var(--blue-pale) 0%, var(--blue-soft) 35%, var(--blue-mid) 68%, var(--blue-deep) 100%);
  }
  .front-stripes {
    position: absolute; left: 0; right: 0; bottom: 14px;
  }
  .front-stripes .band-white { height: 7px; background: var(--white); }
  .front-stripes .band-blue { height: 9px; background: var(--blue-deep); }
  .front-stripes .band-thin { height: 3px; background: var(--white); }
  .front-badge {
    position: absolute; left: 50%; top: 44%;
    transform: translate(-50%, -50%);
    width: 206px; height: 206px;
    border-radius: 50%;
    background: var(--white);
    box-shadow: 0 3px 10px rgba(0,0,0,.25);
    display: flex; align-items: center; justify-content: center;
    text-align: center;
  }
  .brand-name {
    color: var(--blue-deep);
    font-weight: 700;
    letter-spacing: .04em;
    text-transform: uppercase;
  }
  .front-badge .brand-name { font-size: 22px; line-height: 1.2; }

  /* Back side */
  .flyer--back { left: 615px; }
  .photo {
    position: absolute; left: 0; top: 0; width: 100%; height: 190px;
    background: linear-gradient(100deg, #d9dde0 0%, #c9b8a4 30%, #e3d7c8 55%, #2f4a3a 75%, #b9c6cf 100%);
  }
  .back-badge {
    position: absolute; left: 18px; top: 12px;
    width: 84px; height: 84px; border-radius: 50%;
    background: var(--white);
    border: 3px solid #9aa0a8;
    display: flex; align-items: center; justify-content: center;
    text-align: center;
  }
  .back-badge .brand-name { font-size: 10px; line-height: 1.2; }
  .offer {
    position: absolute; right: 0; top: 42px;
    width: 300px;
  }
  .offer__line { height: 3px; background: var(--white); }
  .offer__title {
    margin: 4px 0;
    background: rgba(255,255,255,.92);
    color: var(--blue-deep);
    font-weight: 700;
    font-size: 27px;
    padding: 4px 12px 3px 18px;
    text-align: right;
    letter-spacing: .01em;
  }
  .offer__line--lower { height: 2px; margin-top: 3px; }
  .description {
    position: absolute; left: 22px; right: 22px; top: 194px;
  }
  .description h2 {
    color: var(--blue-mid);
    font-size: 16px;
    font-weight: 700;
    margin-bottom: 3px;
  }
  .description p {
    color: var(--ink);
    font-size: 12px;
    line-height: 1.5;
  }
  .divider {
    position: absolute; left: 22px; right: 22px; top: 300px;
    height: 1px; background: var(--blue-mid);
  }
  .contact {
    position: absolute; left: 22px; right: 22px; top: 310px;
    display: flex; justify-content: space-between; align-items: flex-start;
  }
  .contact__left { display: flex; gap: 18px; align-items: flex-start; }
  .social-square {
    width: 26px; height: 26px; border-radius: 5px;
    background: var(--blue-mid);
    border: 2px solid #c5ccdc;
  }
  .address { font-size: 11.5px; line-height: 1.55; color: var(--ink); }
  .contact__right { text-align: left; }
  .phone { font-size: 18px; font-weight: 700; color: var(--ink); }
  .email { font-size: 11.5px; color: var(--blue-mid); margin-top: 3px; }
  .back-stripes {
    position: absolute; left: 0; right: 0; bottom: 0;
  }
  .back-stripes .band-blue { height: 6px; background: var(--blue-mid); }
  .back-stripes .band-white { height: 4px; background: var(--white); }
  .back-stripes .band-deep { height: 10px; background: var(--blue-deep); }
</style>
</head>
<body>
  <section class="flyer flyer--front" aria-label="Flyer front">
    <div class="front-badge">
      <span class="brand-name">Bright Grove<br>Academy</span>
    </div>
    <div class="front-stripes">
      <div class="band-white"></div>
      <div class="band-blue"></div>
      <div class="band-thin"></div>
    </div>
  </section>

  <section class="flyer flyer--back" aria-label="Flyer back">
    <div class="photo" role="img" aria-label="Photo of a young girl writing at a desk while a teacher guides her hand"></div>
    <div class="back-badge">
      <span class="brand-name">Bright Grove<br>Academy</span>
    </div>
    <div class="offer">
      <div class="offer__line"></div>
      <div class="offer__title">FREE TRIAL CLASS</div>
      <div class="offer__line offer__line--lower"></div>
    </div>

    <div class="description">
      <h2>Description of the centre</h2>
      <p>Bright Grove Academy is where you can develop academic and life skills. Our teachers are the heartbeat of the business. They inspire and nurture students, helping them surpass their expectations. We cover English, Mathematics and Science from Primary and Secondary Levels.</p>
    </div>

    <div class="divider"></div>

    <div class="contact">
      <div class="contact__left">
        <div class="social-square" aria-hidden="true"></div>
        <div class="address">Bright Grove Academy<br>48 Meranti Park Road S512340</div>
      </div>
      <div class="contact__right">
        <div class="phone">6120-4587</div>
        <div class="email">hello@brightgroveacademy.com</div>
      </div>
    </div>

    <div class="back-stripes">
      <div class="band-blue"></div>
      <div class="band-white"></div>
      <div class="band-deep"></div>
    </div>
  </section>
</body>
</html>
```